Accounting business needs business card

I have a business card but need something better. I want the colour changed and the design to be better. I have uploaded a picture of my new sign that is grey in colour, i would like to incorporate these colours.

```html
<!DOCTYPE html>
<html lang="en">
<head>
<meta charset="utf-8">
<title>Nil Ledger – Business Card</title>
<link href="https://fonts.googleapis.com/css2?family=Montserrat:wght@500;600;700&family=Poppins:wght@400;500&display=swap" rel="stylesheet">
<style>
  :root {
    --stage: #2b2b2c;
    --front-dark: #0f2327;
    --front-mid: #1e3b40;
    --silver-light: #f2f2f2;
    --silver-mid: #d6d6d6;
    --silver-dark: #bdbdbd;
    --ink: #1f1f1f;
    --band-dark: #232323;
    --band-grey: #58595b;
    --white: #ffffff;
    --badge-blue: #1a5ea8;
    --badge-yellow: #f3c500;
    --badge-sky: #1ab4e8;
    --badge-lime: #b9d432;
  }
  * { box-sizing: border-box; margin: 0; padding: 0; }
  html, body { width: 1200px; height: 880px; overflow: hidden; }
  body {
    background: var(--stage);
    font-family: "Poppins", sans-serif;
    position: relative;
  }
  .card {
    position: absolute;
    width: 540px;
    height: 310px;
    top: 285px;
    border-radius: 14px;
    overflow: hidden;
    box-shadow: 0 18px 40px rgba(0,0,0,.55);
  }
  /* Front */
  .card-front {
    left: 45px;
    background:
      repeating-linear-gradient(90deg, rgba(255,255,255,.025) 0 1px, transparent 1px 3px),
      linear-gradient(160deg, var(--front-mid), var(--front-dark) 70%);
    display: flex;
    flex-direction: column;
    align-items: center;
    justify-content: center;
    gap: 22px;
  }
  .brand-ring {
    width: 92px; height: 92px;
    border: 3px solid var(--white);
    border-radius: 50%;
  }
  .brand-name {
    font-family: "Montserrat", sans-serif;
    font-weight: 600;
    letter-spacing: 14px;
    color: var(--white);
    font-size: 34px;
    padding-left: 14px;
    white-space: nowrap;
  }
  /* Back */
  .card-back {
    left: 615px;
    background:
      repeating-linear-gradient(90deg, rgba(0,0,0,.03) 0 1px, transparent 1px 3px),
      linear-gradient(135deg, var(--silver-light), var(--silver-mid) 55%, var(--silver-dark));
    color: var(--ink);
  }
  .top-band {
    position: absolute; top: 28px; left: 0; right: 0; height: 22px;
    display: flex;
  }
  .top-band .band-grey { width: 38%; background: var(--band-grey); }
  .top-band .band-name {
    flex: 1; background: var(--band-dark); color: var(--white);
    font-family: "Montserrat", sans-serif; font-weight: 700;
    font-size: 15px; line-height: 22px; padding-left: 14px; letter-spacing: -.3px;
  }
  .credentials {
    position: absolute; top: 56px; left: 221px;
    font-size: 11.5px; line-height: 15px; color: #333;
  }
  .credentials .rule { width: 18px; height: 1.5px; background: var(--ink); margin-top: 10px; }
  .back-brand {
    position: absolute; left: 30px; top: 100px;
    display: flex; flex-direction: column; align-items: center; gap: 10px;
  }
  .back-brand .brand-ring { width: 62px; height: 62px; border: 2.5px solid var(--ink); }
  .back-brand .brand-name {
    color: var(--ink); font-size: 22px; line-height: 26px;
    letter-spacing: 9px; padding-left: 9px;
  }
  .contact {
    position: absolute; left: 250px; top: 108px;
    list-style: none; font-size: 12px; color: #333;
  }
  .contact li { display: flex; align-items: center; gap: 7px; height: 19px; }
  .contact svg { width: 13px; height: 13px; }
  .divider {
    position: absolute; left: 292px; right: 22px; top: 178px; height: 1px; background: var(--ink);
  }
  .registered {
    position: absolute; right: 26px; top: 90px; display: flex; flex-direction: column; align-items: center; gap: 4px;
  }
  .registered .seal {
    width: 54px; height: 54px; border-radius: 50%;
    background: var(--badge-lime); border: 6px solid var(--white); box-shadow: 0 0 0 1px #999;
  }
  .registered p { font-size: 8px; line-height: 9px; text-align: center; }
  .partner {
    position: absolute; left: 232px; top: 199px; height: 50px;
    display: flex; align-items: center; gap: 12px;
  }
  .partner .vline { width: 1px; height: 36px; background: var(--ink); }
  .partner p { font-size: 11.5px; line-height: 14px; white-space: nowrap; }
  .partner .circle { width: 50px; height: 50px; border-radius: 50%; background: var(--badge-sky); }
  .footer-rule { position: absolute; left: 0; right: 0; top: 256px; height: 1px; background: var(--ink); }
  .member-badge {
    position: absolute; left: 22px; top: 264px; width: 124px; height: 36px; display: flex;
  }
  .member-badge span:first-child { flex: 2; background: var(--badge-blue); }
  .member-badge span:last-child { flex: 1; background: var(--badge-yellow); }
</style>
</head>
<body>
  <section class="card card-front" aria-label="Card front">
    <div class="brand-ring"></div>
    <div class="brand-name">NIL LEDGER</div>
  </section>

  <section class="card card-back" aria-label="Card back">
    <div class="top-band">
      <div class="band-grey"></div>
      <div class="band-name">LIAM HARTLEY</div>
    </div>
    <div class="credentials">
      <p>CPA, MTAX, BCOM (Acc &amp; Fin)</p>
      <p>Taxation and Business Accountant</p>
      <div class="rule"></div>
    </div>

    <div class="back-brand">
      <div class="brand-ring"></div>
      <div class="brand-name">NIL LEDGER</div>
    </div>

    <ul class="contact">
      <li>
        <svg viewBox="0 0 16 16" fill="none" stroke="#222" stroke-width="1.3"><circle cx="8" cy="8" r="7"/><path d="M5.5 4.5l1.3 1.6-.8 1c.6 1.2 1.4 2 2.6 2.6l1-.8 1.6 1.3-.8 1.3C7.6 11.4 4.6 8.4 4.2 5.3z"/></svg>
        0412 555 018
      </li>
      <li>
        <svg viewBox="0 0 16 16" fill="none" stroke="#222" stroke-width="1.3"><circle cx="8" cy="8" r="7"/><rect x="4.3" y="5.5" width="7.4" height="5" rx=".5"/><path d="M4.5 6l3.5 2.5L11.5 6"/></svg>
        liam@nilledger.com.au
      </li>
      <li>
        <svg viewBox="0 0 16 16" fill="none" stroke="#222" stroke-width="1.3"><circle cx="8" cy="8" r="7"/><circle cx="8" cy="8" r="3.6"/><path d="M4.4 8h7.2M8 4.4c-1.6 2.2-1.6 5 0 7.2M8 4.4c1.6 2.2 1.6 5 0 7.2"/></svg>
        www.nilledger.com.au
      </li>
    </ul>

    <div class="registered">
      <div class="seal" role="img" aria-label="Registered tax agent seal"></div>
      <p>Tax agent<br>31078552</p>
    </div>

    <div class="divider"></div>

    <div class="partner">
      <div class="vline"></div>
      <p>Nil Ledger is a<br>Member Business</p>
      <div class="circle" role="img" aria-label="Accounting software partner badge"></div>
    </div>

    <div class="footer-rule"></div>
    <div class="member-badge" role="img" aria-label="Professional accounting body membership badge">
      <span></span><span></span>
    </div>
  </section>
</body>
</html>
```